Seafood Retailer requires varies packaging labels

We are an established business (Restaurant, Seafood Retailer and Crayfish Wholesaler). We have just got a new logo which covers all three aspects of our business (via Artbazaar!). We have always sold cellar door but have been asked by several food outlets to stock our product but as you will see from our pictures - it needs some serious work to take us to the next level. We have a well known finer dining restaurant which we use all these products in and is how several products came about on our Seafood shop shelves. The products are of high quality (just not the labelling). We now want to package our Seafood Retail Shop with professional packaging and labelling and reflect the "quality and freshness" of our products. We have several items we want to label as per below.

If we were to use a slogan it would be "Its about the Freshness and Quality" but not necessary.

We are after a label for our Pickled Seafood 350g tub (Various) - conical container 9cm high x 9cm (top), 7cm (bottom) ONLY but will also try and utilise it to be consistent with the other products following.

Salt and Pepper MIx 250g - conical container (as above)
Smoked Fish (Various weight & fish) - 21cm x 25cm vacuum sealed bags.
Kilpatrick Sauce 250ml - square bottle 22cm high x 4.5cm wide
Minty Lime Vinaigrette 250ml - 23cm round bottle - 4.7cm dia.
Smoked Spicy Salt 75g- 13cm wide x 16cm high vacuum bag
Dukkah 75g - 13cm wide x 16cm high vacuum bag
Lobster Oil 150ml - 18cm x 4.5cm dia round bottle

We will need a working file so we can change the names for the pickled seafood as needed.

I have attached photos of our current products for true understanding of what we currently have had to get by and where we wish to go.

We have a label printer that can print black type overs eg the name of each product so we can have generic coloured labels which we can print over with the change of each product.

We want something that will become a recognisable label.
Updates

Attn Designers.
We are only after one design but which we will use as a guide for all the options supplied as a starting point. The Pickled containers will probably be where we start but happy with any submissions. I probably wasnt very clear but wanted to show all the things we will be using the labelling for so that we can get some continuity We are just after some direction on a good look.  Thanks Melda

Reason: Had some technical problems and wish to extend the time to allow more time conversing with designers.

Target Market(s)

Our target market varies but generally 30 - 65 years in the more affluent background. We are located "literally in the middle of a paddock in the middle of nowhere" (near several holiday villages) and it is the reputation of our premium, fresh products that have people returning and amazed on their first experience.

Industry/Entity Type

Restaurant

Requirements
Must have
• All:

Our logo and the colours are:
Orange
C 13%
M 79%
Y 100%
K 3%

Blue
C 100%
M 96%
Y 14%
K 3%

weight

nutrition panel, barcode (but we can also do that as a separate label on the back ourselves if needed)

"Produced & packaged by:
Copper Reef Foods Pty Ltd, 40271 Danvers Highway, Millicoon SA 5630
Ph: 08 87316042"

Made in Australia from local and imported ingredients. Keep refrigerated. Store at 1oC - 4oC. Use in 7 days after opening.

Nice to have
• Pickled seafood - "Gourmet Pickled" and "Ready to Eat"
Should not have
• Use only the "Copper Reef Foods" logo (not the "Copper Reef Restaurant & Seafood Sales or Restaurant Only logos)

```html
<!DOCTYPE html>
<html lang="en">
<head>
<meta charset="utf-8">
<title>Copper Reef Foods — Label Concepts</title>
<link rel="stylesheet" href="https://fonts.googleapis.com/css2?family=Cabin:wght@600;700&display=swap">
<style>
  :root {
    --orange: #c4643a;
    --orange-deep: #c0683e;
    --frame-line: #c8754e;
    --panel-edge: #e2b69e;
    --sea: #cfd7ee;
    --sea-light: #e6eaf6;
    --shadow: #e4e4ea;
    --paper: #ffffff;
  }
  * { margin: 0; padding: 0; box-sizing: border-box; }
  html, body {
    width: 951px;
    height: 1200px;
    overflow: hidden;
    background: var(--paper);
  }
  .canvas {
    position: relative;
    width: 951px;
    height: 1200px;
    font-family: "Cabin", "Segoe UI", sans-serif;
  }
  .label-concept {
    position: absolute;
    left: 49px;
    width: 866px;
    height: 449px;
    display: block;
  }
  .label-concept--plain { top: 58px; }
  .label-concept--slogan { top: 546px; }
  .panel-edge { fill: var(--paper); stroke: var(--panel-edge); stroke-width: 2; }
  .sea-band { fill: var(--sea); }
  .sea-stripe { fill: var(--sea-light); }
  .frame-shadow { fill: var(--shadow); }
  .frame { fill: var(--paper); }
  .frame-outline { fill: none; stroke: var(--frame-line); stroke-width: 3; }
  .slogan-band { fill: var(--orange-deep); }
  .brand-name {
    font-family: "Cabin", "Segoe UI", sans-serif;
    font-weight: 700;
    font-size: 58px;
    letter-spacing: 1px;
    fill: var(--orange);
  }
  .product-name {
    font-family: "Cabin", "Segoe UI", sans-serif;
    font-weight: 700;
    font-size: 24px;
    letter-spacing: 1px;
    fill: var(--orange);
  }
  .product-detail {
    font-family: "Cabin", "Segoe UI", sans-serif;
    font-weight: 600;
    font-size: 18px;
    fill: var(--orange);
  }
  .producer {
    font-family: "Cabin", "Segoe UI", sans-serif;
    font-weight: 600;
    font-size: 13px;
    fill: var(--orange);
  }
  .slogan {
    font-family: "Cabin", "Segoe UI", sans-serif;
    font-weight: 700;
    font-size: 32px;
    fill: var(--paper);
  }
  .designer-note {
    position: absolute;
    left: 86px;
    top: 1062px;
    width: 800px;
    font-weight: 700;
    font-size: 31px;
    line-height: 45px;
    color: var(--orange);
  }
</style>
</head>
<body>
<main class="canvas">
  <svg class="label-concept label-concept--plain" viewBox="0 0 866 449" aria-label="Label concept without slogan">
    <defs>
      <path id="frame-shape" d="M69,23 H799 A40,40 0 0 0 839,63 V377 A40,40 0 0 0 799,417 H69 A40,40 0 0 0 29,377 V63 A40,40 0 0 0 69,23 Z"/>
    </defs>
    <rect class="panel-edge" x="1" y="1" width="864" height="447"/>
    <rect class="sea-stripe" x="2" y="234" width="862" height="12"/>
    <rect class="sea-band" x="2" y="246" width="862" height="201"/>
    <use href="#frame-shape" class="frame-shadow" transform="translate(-7,7)"/>
    <use href="#frame-shape" class="frame"/>
    <use href="#frame-shape" class="frame-outline"/>
    <text class="brand-name" x="433" y="160" text-anchor="middle">Copper Reef Foods</text>
    <text class="product-name" x="433" y="232" text-anchor="middle">Gourmet Pickled Seafood</text>
    <text class="product-detail" x="433" y="262" text-anchor="middle">Ready to Eat · 350g</text>
    <text class="producer" x="433" y="350" text-anchor="middle">Produced &amp; packaged by: Copper Reef Foods Pty Ltd, 40271 Danvers Highway, Millicoon SA 5630</text>
    <text class="producer" x="433" y="370" text-anchor="middle">Ph: 08 87316042 · Made in Australia from local and imported ingredients · Keep refrigerated 1°C – 4°C</text>
  </svg>

  <svg class="label-concept label-concept--slogan" viewBox="0 0 866 449" aria-label="Label concept with slogan band">
    <defs>
      <path id="frame-shape-2" d="M69,23 H799 A40,40 0 0 0 839,63 V377 A40,40 0 0 0 799,417 H69 A40,40 0 0 0 29,377 V63 A40,40 0 0 0 69,23 Z"/>
      <clipPath id="frame-clip"><use href="#frame-shape-2"/></clipPath>
    </defs>
    <rect class="panel-edge" x="1" y="1" width="864" height="447"/>
    <rect class="sea-stripe" x="2" y="234" width="862" height="12"/>
    <rect class="sea-band" x="2" y="246" width="862" height="201"/>
    <use href="#frame-shape-2" class="frame-shadow" transform="translate(-7,7)"/>
    <use href="#frame-shape-2" class="frame"/>
    <rect class="slogan-band" x="20" y="318" width="830" height="104" clip-path="url(#frame-clip)"/>
    <use href="#frame-shape-2" class="frame-outline"/>
    <text class="brand-name" x="433" y="148" text-anchor="middle">Copper Reef Foods</text>
    <text class="product-name" x="433" y="212" text-anchor="middle">Gourmet Pickled Seafood</text>
    <text class="product-detail" x="433" y="240" text-anchor="middle">Ready to Eat · 350g</text>
    <text class="producer" x="433" y="276" text-anchor="middle">Produced &amp; packaged by: Copper Reef Foods Pty Ltd, 40271 Danvers Highway, Millicoon SA 5630</text>
    <text class="producer" x="433" y="296" text-anchor="middle">Ph: 08 87316042 · Made in Australia from local and imported ingredients · Keep refrigerated 1°C – 4°C</text>
    <text class="slogan" x="433" y="378" text-anchor="middle">It's all about Freshness and Quality</text>
  </svg>

  <p class="designer-note">Let me know what sizes you want them in before I send them. It was unclear in the brief. Cheers :)</p>
</main>
</body>
</html>
```